Official personalized stationery with official coat of arms

I am looking for custom stationery design such as US letter size (8.5 X 11 or 21.6cm X 27.9cm), email signature (email) and envelope for US letter size (standard envelope no. 10 or 10.5cm X 24.5cm). Inspired by my personal coat of arms and my postal address:

4186 rue des Tilleuls
Belleval, Ontario, H2K 4P7
Canada

Ideally a discreet design based on the coat of arms of Lucien Morvan but inspired by my mother's original coat of arms.

Something golden and translucent, simple but tasteful, without overemphasizing the green color. The coat of arms should have green, but not the entire structure of the stationery.

I am also looking for a small official thank you card in half letter size.

The design must be with the Lucien Morvan coat of arms and not the full coat of arms

Target Market(s)

For official communication

Industry/Entity Type

Communication officiel et parlementaire

Font styles to use
Other font styles liked:
• J’aime bien l’écriture comme le logo de la maison Delorme la police pour écrire le nom Delorme

Requirements
Must have
• Simplicity and use the Lucien Morvan coat of arms and not the full coat of arms
Nice to have
• Official and royal appearance as it is an official heraldic title of the British crown
Should not have
• Email and website

```html
<!DOCTYPE html>
<html lang="fr">
<head>
<meta charset="utf-8">
<title>Lucien Morvan — Stationery</title>
<link href="https://fonts.googleapis.com/css2?family=Pinyon+Script&family=Libre+Baskerville:wght@400&family=Open+Sans:wght@400&display=swap" rel="stylesheet">
<style>
  :root{
    --green:#1f4d28;
    --gold:#b8863b;
    --bg-left:#e3e3e3;
    --bg-right:#b9b9b9;
    --paper:#ffffff;
    --edge:rgba(0,0,0,.08);
  }
  *{box-sizing:border-box;margin:0;padding:0}
  html,body{width:1200px;height:548px;overflow:hidden}
  body{position:relative;background:var(--bg-left);font-family:"Libre Baskerville",serif}
  .panel-right{position:absolute;left:686px;top:0;width:514px;height:548px;background:var(--bg-right)}
  .sheet{position:absolute;background:var(--paper);box-shadow:0 1px 3px var(--edge)}
  .label{position:absolute;font-family:"Open Sans",sans-serif;font-size:7px;letter-spacing:.04em;color:var(--green);text-transform:uppercase}
  .script{font-family:"Pinyon Script",cursive;color:var(--gold);white-space:nowrap}
  .address{font-family:"Libre Baskerville",serif;color:var(--green);text-transform:uppercase;white-space:nowrap;letter-spacing:.03em}
  .address span+span{margin-left:1.4em}
  .mark{display:flex;align-items:center;gap:4px;color:var(--green);font-family:"Libre Baskerville",serif;text-transform:uppercase;letter-spacing:.06em;white-space:nowrap}
  .mark::before{content:"";display:block;width:var(--sq,12px);height:var(--sq,12px);background:currentColor}
  .center{display:flex;flex-direction:column;align-items:center}

  /* letterhead */
  .letterhead{left:40px;top:36px;width:232px;height:300px}
  .letterhead .head{position:absolute;top:22px;left:0;right:0;gap:4px}
  .letterhead .mark{font-size:6px;--sq:11px}
  .letterhead .script{font-size:13px}
  .letterhead .address{position:absolute;bottom:16px;left:0;right:0;text-align:center;font-size:4.2px}

  /* name cards */
  .card-front{left:330px;top:52px;width:170px;height:98px;justify-content:center;gap:8px}
  .card-front .script{font-size:15px}
  .card-front .address{font-size:3.6px}
  .card-back{left:330px;top:164px;width:170px;height:98px;background:var(--green);justify-content:center}
  .card-back .mark{color:var(--paper);font-size:7px;--sq:12px}

  /* envelope */
  .envelope{left:300px;top:296px;width:330px;height:146px}
  .envelope .mark{position:absolute;right:22px;top:18px;font-size:5.5px;--sq:11px}
  .envelope .return{position:absolute;left:22px;bottom:18px;gap:3px;align-items:flex-start}
  .envelope .script{font-size:12px}
  .envelope .address{font-size:3.8px}

  /* thank you set */
  .folded{left:786px;top:74px;width:140px;height:206px}
  .folded .fold{position:absolute;left:0;right:0;top:50%;height:1px;background:rgba(0,0,0,.08)}
  .folded .sign{position:absolute;left:0;right:0;bottom:10px;gap:2px}
  .folded .from{font-size:2.6px;color:var(--green);letter-spacing:.08em;text-transform:uppercase}
  .folded .script{font-size:7px}
  .folded .address{font-size:2.3px}
  .merci{left:950px;top:66px;width:142px;height:104px;justify-content:center}
  .merci .frame{position:absolute;inset:5px;border:.6px solid var(--gold)}
  .merci .script{font-size:15px}
  .small-env{left:950px;top:182px;width:148px;height:108px;overflow:hidden}
  .small-env svg{position:absolute;inset:0}
  .small-env .mark{position:absolute;left:0;right:0;top:20px;justify-content:center;font-size:3.5px;--sq:7px}

  /* email header */
  .email{left:768px;top:356px;width:348px;height:88px;display:flex;align-items:center;padding:0 28px;gap:14px}
  .email .mark{font-size:6px;--sq:26px;flex-direction:column;gap:3px}
  .email .script{font-size:13px}
  .email .address{font-size:3.8px}
</style>
</head>
<body>
  <div class="panel-right"></div>

  <section class="sheet letterhead">
    <div class="head center">
      <div class="mark">Lucien Morvan</div>
      <div class="script">Lucien Morvan</div>
    </div>
    <p class="address"><span>4186 rue des Tilleuls</span><span>Belleval, Ontario, H2K 4P7</span><span>Canada</span></p>
  </section>
  <p class="label" style="left:118px;top:428px">Letter head</p>

  <section class="sheet card-front center">
    <div class="script">Lucien Morvan</div>
    <p class="address"><span>4186 rue des Tilleuls</span><span>Belleval, Ontario, H2K 4P7</span><span>Canada</span></p>
  </section>
  <section class="sheet card-back center">
    <div class="mark">Lucien Morvan</div>
  </section>
  <p class="label" style="left:514px;top:203px">Name card</p>

  <section class="sheet envelope">
    <div class="mark">Lucien Morvan</div>
    <div class="return center">
      <div class="script">Lucien Morvan</div>
      <p class="address"><span>4186 rue des Tilleuls</span><span>Belleval, Ontario, H2K 4P7</span><span>Canada</span></p>
    </div>
  </section>
  <p class="label" style="left:437px;top:490px">Envelope</p>

  <section class="sheet folded">
    <div class="fold"></div>
    <div class="sign center">
      <p class="from">Du bureau de</p>
      <div class="script">Lucien Morvan</div>
      <p class="address"><span>4186 rue des Tilleuls</span><span>Belleval, Ontario, H2K 4P7</span><span>Canada</span></p>
    </div>
  </section>
  <section class="sheet merci center">
    <div class="frame"></div>
    <div class="script">Merci</div>
  </section>
  <section class="sheet small-env">
    <svg width="148" height="108" viewBox="0 0 148 108" aria-hidden="true">
      <polyline points="0,108 60,58 88,58 148,108" fill="none" stroke="rgba(0,0,0,.07)" stroke-width="1"/>
      <path d="M0 0 L66 50 Q74 56 82 50 L148 0" fill="#fafafa" stroke="rgba(0,0,0,.09)" stroke-width="1"/>
    </svg>
    <div class="mark">Lucien Morvan</div>
  </section>
  <p class="label" style="left:906px;top:312px">Thank you card</p>

  <section class="sheet email">
    <div class="mark">Lucien Morvan</div>
    <div class="script">Lucien Morvan</div>
    <p class="address"><span>4186 rue des Tilleuls</span><span>Belleval, Ontario, H2K 4P7</span><span>Canada</span></p>
  </section>
  <p class="label" style="left:918px;top:466px">Email header</p>
</body>
</html>
```